Business Card Design Project

I am looking for a classy business card design for a product design consultancy. We specialize in Product Design, Prototyping, and Manufacturing Consulting. Products that we design range from consumer electronics to household products all the way to sporting goods. We are based in Arizona and called "Pelican Forge Studio." We like to have fun and goof off as much as we like to create new products. We are young and energetic so we would like our business cards to reflect that. We already have a logo that we would like to implement into the card design. A plain rectangular business card is boring so feel free to get creative, but please, no avocado shaped cards (it's far too literal). Also feel free to play around with textured card stocks or plastic. The final design that we choose will pay attention to all of the little details. Our cards will need to be 2 sided. We're giving you guys free reign to design as you would like. Please have fun with this, it will reflect in our business card.

Thanks guys,
Pelican Forge Studio Team
Updates

Industry/Entity Type

Electronics

Requirements
Must have
• We would like to have a spot UV coating somewhere on the business card design if possible.
Nice to have
• Let's see some designs with custom shapes rather than typical rectangular business cards but please no avocado shaped cards, thanks. Also play around with textured card socks.

Files

```html
<!DOCTYPE html>
<html lang="en">
<head>
<meta charset="utf-8">
<title>Pelican Forge Studio — Business Card</title>
<link rel="stylesheet" href="https://fonts.googleapis.com/css2?family=Nunito:wght@800&family=Arimo:wght@400;700&display=swap">
<style>
  :root {
    --leaf: #8cc63f;
    --paper: #f7f7f5;
    --ink: #4a4a4a;
    --backdrop: #d9dcd6;
    --white: #ffffff;
  }
  * { margin: 0; padding: 0; box-sizing: border-box; }
  html, body { width: 1200px; height: 900px; overflow: hidden; }
  body {
    background: var(--backdrop);
    position: relative;
    font-family: "Arimo", Arial, sans-serif;
  }
  .card {
    position: absolute;
    left: 320px;
    width: 560px;
    height: 320px;
    border-radius: 16px;
    overflow: hidden;
    box-shadow: 0 6px 18px rgba(0,0,0,0.18);
  }
  .card svg.wave { position: absolute; inset: 0; width: 100%; height: 100%; }
  .card-front { top: 100px; background: var(--leaf); }
  .card-back { top: 480px; background: var(--paper); }

  .brand {
    position: absolute;
    font-family: "Nunito", "Arial Rounded MT Bold", sans-serif;
    font-weight: 800;
    letter-spacing: 0.5px;
    display: flex;
    align-items: center;
    gap: 10px;
    white-space: nowrap;
    line-height: 1;
  }
  .brand-dot { width: 26px; height: 26px; border-radius: 50%; background: currentColor; flex: none; }
  .brand-front { left: 52px; top: 104px; font-size: 34px; color: var(--white); }
  .brand-back-top { left: 26px; top: 26px; font-size: 26px; color: var(--leaf); }
  .brand-back-top .brand-dot { width: 20px; height: 20px; }
  .brand-back-bottom { right: 26px; bottom: 22px; font-size: 26px; color: var(--white); }
  .brand-back-bottom .brand-dot { width: 20px; height: 20px; }

  .contact-list {
    position: absolute;
    left: 24px;
    top: 108px;
    list-style: none;
    font-size: 13.5px;
    letter-spacing: 1.4px;
    color: var(--ink);
    line-height: 19px;
  }
  .contact-list li { display: flex; align-items: center; gap: 8px; }
  .contact-list svg { width: 11px; height: 11px; fill: var(--ink); flex: none; }

  .holder { position: absolute; right: 30px; top: 104px; text-align: right; }
  .holder-name { font-weight: 700; font-size: 19px; letter-spacing: 1.2px; color: var(--leaf); }
  .holder-role { font-size: 13px; letter-spacing: 1px; color: var(--ink); margin-top: 3px; }
</style>
</head>
<body>

<section class="card card-front" aria-label="Card front">
  <svg class="wave" viewBox="0 0 560 320" preserveAspectRatio="none" aria-hidden="true">
    <path fill="#ffffff" d="M0,205 C90,265 200,250 300,205 C390,165 480,140 560,136 C480,146 400,175 310,225 C210,282 90,300 0,240 Z"/>
  </svg>
  <div class="brand brand-front"><span class="brand-dot"></span>pelican forge studio</div>
</section>

<section class="card card-back" aria-label="Card back">
  <svg class="wave" viewBox="0 0 560 320" preserveAspectRatio="none" aria-hidden="true">
    <path fill="#8cc63f" d="M0,178 C60,235 150,250 260,240 C370,230 460,205 560,205 L560,320 L0,320 Z"/>
    <path fill="#f7f7f5" d="M0,197 C60,248 150,258 260,247 C370,236 460,215 560,215 L560,224 C460,224 370,246 260,257 C150,268 60,262 0,216 Z"/>
  </svg>

  <div class="brand brand-back-top"><span class="brand-dot"></span>pelican forge studio</div>

  <ul class="contact-list">
    <li><svg viewBox="0 0 12 12"><path d="M2 1h3l1 3-2 1c1 2 2 3 4 4l1-2 3 1v3c-6 0-10-4-10-10z"/></svg>480 555 0137</li>
    <li><svg viewBox="0 0 12 12"><rect x="3" y="0" width="6" height="12" rx="1"/></svg>602 555 0184</li>
    <li><svg viewBox="0 0 12 12"><path d="M0 2h12v8H0z M0 2l6 5 6-5"/></svg>dean@pelicanforgestudio.com</li>
    <li><svg viewBox="0 0 12 12"><circle cx="6" cy="6" r="6"/></svg>www.pelicanforgestudio.com</li>
  </ul>

  <div class="holder">
    <p class="holder-name">Dean Calloway</p>
    <p class="holder-role">President</p>
  </div>

  <div class="brand brand-back-bottom"><span class="brand-dot"></span>pelican forge studio</div>
</section>

</body>
</html>
```